VelmiTaro 16 pages booklet CD Cover

I need a cover (also formatted to be used for digital release), a 16 Pages Booklet + Inlay both sides, a back cover, and a CD image for french pop-rock album.

The name of the artist : Velmitaro
The name of the album : Marcher sous la brume (which means "walking under the mist")
Style of music: I've attached some mp3 extracts. In a few words, this is electro POP music, I'm inspired by band such as The Haze, etc..

This album talks about the desire to live elsewhere, in a world more just and equitable, less painful. The songs talk about people fighting to find a job, to feed their son, poeple who would like to have enough money to enjoy life, etc... but as they can't, at least, they dream about a new world, they draw this elsewhere, hence the title of the album "Marcher sous la brume"

Font styles to use
Sans Serif

Colors
b768aa
33a6d7

Requirements
Must have
• COver: fell free to make your porposal as long as it match the project description objectoves.
• I have add/attached a document "CD Cover Structure" that explains the stucture of the cover, and how i think it could be setup. BUt any other proposal will be welcome.
• For the last one, we will put the song titles and i will let you make me some suggestions.
Nice to have
• the songs are rather melancholy (but not sad) and it would be nice to transmit this impression by the colors. That's why i have chose the pink and blue as primary colours.

```html
<!DOCTYPE html>
<html lang="fr">
<head>
<meta charset="utf-8">
<title>VelmiTaro — Marcher sous la brume — livret</title>
<link rel="stylesheet" href="https://fonts.googleapis.com/css2?family=Questrial&family=Cousine&display=swap">
<style>
  :root{
    --blue:#33a6d7;
    --purple:#b768aa;
    --ink-blue:#1f6fa8;
    --text:#2a2a2a;
    --pink:#e0226a;
    --paper:#ffffff;
    --sky-light:#d6ecf7;
    --sky:#8ecbe8;
  }
  *{box-sizing:border-box;margin:0;padding:0}
  html,body{width:1200px;height:1200px;overflow:hidden;background:#fff}
  body{position:relative;font-family:"Questrial",sans-serif;color:var(--text)}
  .spread{position:absolute;border:1px solid #777;overflow:hidden}
  .spread--top{left:90px;top:94px;width:994px;height:498px}
  .spread--bottom{left:90px;top:634px;width:996px;height:498px}
  .page{position:absolute;top:0;height:100%;overflow:hidden}

  /* Lyrics page */
  .lyrics{left:0;width:496px;background:var(--paper)}
  .lyrics__stripe{position:absolute;top:0;height:100%;width:12px}
  .lyrics__stripe--blue{left:0;background:var(--blue)}
  .lyrics__stripe--purple{left:12px;background:var(--purple)}
  .lyrics__globe{position:absolute;left:196px;top:208px;width:256px;height:256px;border-radius:50%;
    background:radial-gradient(circle at 45% 55%,rgba(240,170,200,.45) 0 28%,rgba(190,225,245,.45) 40%,rgba(245,245,245,.5) 70%,rgba(255,255,255,0) 72%)}
  .lyrics__title{position:absolute;left:68px;top:18px;font-size:21px;color:var(--ink-blue);font-weight:400}
  .lyrics__author{position:absolute;left:68px;top:42px;font-family:"Cousine",monospace;font-size:9.5px;color:#333}
  .lyrics__body{position:absolute;left:68px;top:86px;font-size:7.8px;line-height:10.6px;color:#333}
  .lyrics__body p{margin-bottom:10px}
  .lyrics__body p.first{margin-bottom:20px}

  /* Photo pages */
  .photo{position:absolute;inset:0}
  .photo--studio{background:linear-gradient(160deg,#6a5a4a 0%,#b28a62 35%,#5a3e2a 70%,#2a1c14 100%)}
  .photo--session{background:linear-gradient(200deg,#8a6a4a 0%,#4a3424 40%,#2a1c14 75%,#6a2a20 100%)}
  .thanks-right{left:496px;width:498px}
  .thanks-left{left:0;width:498px}
  .note{position:absolute;background:rgba(255,255,255,.82);color:#222;font-size:12.4px;line-height:15.4px;text-align:justify}
  .note--first{left:36px;top:32px;width:228px;height:356px;padding:22px 8px 0 8px}
  .note--second{left:20px;top:24px;width:228px;height:280px;padding:16px 10px 0 12px}
  .note__heading{font-size:14.5px;line-height:18px;font-weight:400;color:var(--ink-blue);text-align:center;margin-bottom:18px}
  .note p{text-indent:16px}
  .note p.cont{text-indent:0}
  .brand{position:absolute;display:flex;align-items:center;gap:5px;font-size:15px;color:var(--pink)}
  .brand__dot{width:14px;height:14px;border-radius:50%;background:var(--pink)}
  .brand--top{left:360px;top:34px}
  .brand--bottom{left:368px;top:36px}

  /* Tracklist page */
  .tracks{left:500px;width:496px;background:linear-gradient(180deg,var(--sky-light),var(--sky) 60%,#b9def0)}
  .tracks__band{position:absolute;left:108px;top:0;width:278px;height:100%;background:rgba(255,255,255,.35)}
  .tracks__child{position:absolute;left:2px;top:174px;width:208px;height:320px;
    background:linear-gradient(180deg,rgba(90,120,160,.15),rgba(70,100,140,.45));border-radius:40% 50% 0 0}
  .tracks__globe{position:absolute;left:282px;top:270px;width:208px;height:224px;border-radius:50%;
    background:radial-gradient(circle at 40% 55%,rgba(220,30,100,.8) 0 30%,rgba(51,166,215,.8) 42%,rgba(255,255,255,.6) 62%,rgba(255,255,255,0) 66%)}
  .tracklist{position:absolute;left:0;top:44px;width:100%;list-style:none;text-align:center;color:var(--ink-blue)}
  .tracklist li{font-size:16px;line-height:20px;margin-top:3px}
  .tracklist li .num{display:inline-block;margin-right:14px}
  .tracklist .dedication{font-size:10.5px;line-height:13px;color:#222;margin-top:0}
</style>
</head>
<body>

<section class="spread spread--top">
  <article class="page lyrics">
    <div class="lyrics__stripe lyrics__stripe--blue"></div>
    <div class="lyrics__stripe lyrics__stripe--purple"></div>
    <div class="lyrics__globe" role="img" aria-label="Globe terrestre pâle en rose et bleu"></div>
    <h1 class="lyrics__title">A vous tous</h1>
    <p class="lyrics__author">(Odile Marchand-Velmitaro)</p>
    <div class="lyrics__body">
      <p class="first">A ceux d’hier, à ceux d’ici,<br>A mes voisins, parfois d’un soir<br>Je voudrais dire à vous tous qui portez mes jours<br>du bout du cœur, Un doux merci.</p>
      <p>Je suis tissé de ces moments<br>De ces éclats de lumière<br>Que vous m’offrez, m’offrez sans compter<br>Mais ils passent si vite.<br>Légers et vite.</p>
      <p>Et si l’on s’est perdu de vue<br>J’aimerais d’un refrain dissiper ce ciel de plomb<br>sur la tristesse poser le jour<br>Sur la pierre la mousse, la mousse</p>
      <p>Je suis tissé de ces moments<br>De ces éclats de lumière<br>Que vous m’offrez, m’offrez sans compter<br>Mais ils passent si vite.<br>Légers et vite</p>
    </div>
  </article>

  <article class="page thanks-right">
    <div class="photo photo--studio" role="img" aria-label="Photo d’un studio de musique avec guitares suspendues au mur"></div>
    <div class="brand brand--top"><span class="brand__dot"></span>VelmiTaro</div>
    <div class="note note--first">
      <h2 class="note__heading">Je voudrais dire merci à tous ceux qui ont aidé à mettre en chansons ces fragments de moi</h2>
      <p>«Je voudrais dire merci à tous ceux qui ont aidé à mettre en chansons ces fragments de moi.</p>
      <p>D’abord un immense merci à Paul Verrat, un auteur et un homme rare pour qui j’ai une grande estime et qui a su poser en mots mes rêves et mes doutes. Merci aussi à Odile Marchand, une plume avec qui j’aimerais écrire davantage sur un prochain disque.</p>
      <p>Un grand merci encore à Henri Castel, le musicien qui a arrangé, programmé et joué tous les</p>
    </div>
  </article>
</section>

<section class="spread spread--bottom">
  <article class="page thanks-left">
    <div class="photo photo--session" role="img" aria-label="Photo d’une session d’enregistrement avec chaise en cuir et guitare"></div>
    <div class="brand brand--bottom"><span class="brand__dot"></span>VelmiTaro</div>
    <div class="note note--second">
      <p class="cont">instruments, y compris les chœurs que l’on entend sur « Lumière de novembre ». Sans cette belle rencontre, ce disque n’aurait jamais eu cette couleur ni ce son.</p>
      <p>Enfin, un grand merci à Luca Ferrani pour son aide lors des prises de voix et pour le superbe chœur sur « Debout les rêveurs ». Merci aussi à Thierry Morlan pour les cours de chant. J’aurais aimé pouvoir les poursuivre.</p>
      <p>L’album a été mixé au studio Orel. Merci à toute l’équipe »</p>
    </div>
  </article>

  <article class="page tracks">
    <div class="tracks__band"></div>
    <div class="tracks__child" role="img" aria-label="Illustration d’un enfant dessinant des cœurs au mur"></div>
    <div class="tracks__globe" role="img" aria-label="Globe en pièces de puzzle rose et bleu"></div>
    <ol class="tracklist">
      <li><span class="num">1</span>Lumière de novembre</li>
      <li><span class="num">2</span>Debout les rêveurs!</li>
      <li class="dedication">(aux oubliés, aux sans-voix et aux rêveurs)</li>
      <li><span class="num">3</span>Retenir l’heure</li>
      <li class="dedication">(à ma fille qui grandit trop vite)</li>
      <li><span class="num">5</span>Un autre matin</li>
      <li><span class="num">6</span>Marcher sous la brume</li>
      <li><span class="num">7</span>Je traverse</li>
      <li><span class="num">8</span>Le fanal</li>
      <li><span class="num">9</span>Le vent a tourné</li>
      <li class="dedication">(à Rosa, Milan, Yves, etc…)</li>
      <li><span class="num">10</span>A vous tous</li>
    </ol>
  </article>
</section>

</body>
</html>
```